Business Card Design Project

Hello
I want a Simple Business card that uses the company logo that is easily reasonable but looks professional as I am an IT Services company and would look to share these cards with prospective clients.
The details are:
Kelvo Ridge Solutions
14 Marlow Crescent
Birmingham
B7 4QT
Telephone 0845 271 6049
I would like my name Gareth Wilcombe and my title Director on the card.
Target Market(s)
IT Professionals
Industry/Entity Type
Business

```html
<!DOCTYPE html>
<html lang="en">
<head>
<meta charset="utf-8">
<title>Kelvo Ridge Solutions – Business Card</title>
<link rel="stylesheet" href="https://fonts.googleapis.com/css2?family=PT+Sans:wght@400;700&display=swap">
<style>
  :root {
    --card-bg: #cb7245;
    --text-cream: #fdf3a7;
    --accent-peach: #f7a86f;
    --brand-dark: #3b3a3a;
    --brand-leaf: #9ccf6e;
  }
  html, body {
    margin: 0;
    padding: 0;
    overflow: hidden;
    background: #ffffff;
  }
  .card {
    position: relative;
    width: 1200px;
    height: 707px;
    background: var(--card-bg);
    font-family: "PT Sans", Arial, sans-serif;
    color: var(--text-cream);
    overflow: hidden;
  }
  .brand {
    position: absolute;
    top: 40px;
    right: 74px;
    display: flex;
    align-items: center;
    gap: 12px;
  }
  .brand-dot {
    width: 34px;
    height: 34px;
    border-radius: 50%;
    background: var(--brand-leaf);
  }
  .brand-name {
    font-size: 40px;
    font-weight: 700;
    color: var(--brand-dark);
    line-height: 1;
    letter-spacing: -0.5px;
  }
  .holder {
    position: absolute;
    left: 57px;
    top: 170px;
    margin: 0;
    font-size: 42px;
    font-weight: 400;
    line-height: 1;
  }
  .address {
    position: absolute;
    left: 524px;
    top: 286px;
    margin: 0;
    font-style: normal;
    font-size: 44px;
    line-height: 58px;
  }
  .phone {
    position: absolute;
    left: 549px;
    top: 596px;
    margin: 0;
    font-size: 44px;
    line-height: 1;
  }
  .ornament {
    position: absolute;
    left: 0;
    top: 290px;
  }
</style>
</head>
<body>
  <div class="card">
    <div class="brand">
      <span class="brand-dot"></span>
      <span class="brand-name">Kelvo Ridge</span>
    </div>

    <h1 class="holder">Gareth Wilcombe (Director)</h1>

    <address class="address">
      Kelvo Ridge Solutions<br>
      14 Marlow Crescent<br>
      Birmingham, B7 4QT
    </address>

    <p class="phone">Telephone: 0845 271 6049</p>

    <svg class="ornament" width="450" height="417" viewBox="0 0 450 417" role="img" aria-label="Decorative cluster of peach pinwheel star ornaments along the lower-left corner">
      <defs>
        <radialGradient id="ornament-glow" cx="0.3" cy="0.75" r="0.8">
          <stop offset="0" stop-color="#f7a86f" stop-opacity="0.9"/>
          <stop offset="1" stop-color="#f7a86f" stop-opacity="0.25"/>
        </radialGradient>
      </defs>
      <rect x="0" y="0" width="160" height="417" rx="40" fill="url(#ornament-glow)"/>
      <rect x="160" y="262" width="290" height="155" rx="40" fill="url(#ornament-glow)"/>
    </svg>
  </div>
</body>
</html>
```